Gutschein-Design für Baumhaus-Vermietung
Zielgruppe
Das Leben in einem Baumhaus verspricht Entspannung, Abenteuer, Entdeckungen, Spaß, Spiel und Naturbeobachtungen. Unsere gemütlichen Baumhäuser bieten Ihnen einen naturverbundenen Urlaub mit vielen aufregenden Erlebnissen.
Aufgabenstellung
Das Logo soll unbedingt verwendet werden. Das Format sollte DIN a4 sein, dass wir es über unseren Drucker erstellen können. Als Angaben auf dem Gutschein zur Identifikation wird eine Gutscheinnummer und ein Ausstellungsdatum benötigt. Dazu unsere Adresse und die Kontaktdaten. Es handelt sich um einen Wertgutschein (der dann als Urlaubscheck eingelöst werden kann)

```html
<!DOCTYPE html>
<html lang="de">
<head>
<meta charset="utf-8">
<title>Gutschein – Waldnest Baumhausdorf</title>
<link href="https://fonts.googleapis.com/css2?family=Kaushan+Script&family=Source+Serif+4:wght@400;600&display=swap" rel="stylesheet">
<style>
  :root {
    --canvas: #e8e8e8;
    --paper: #f5f5f5;
    --forest: #2e7d4f;
    --bark: #7a5a3a;
    --bark-text: #8a6a4a;
    --ink: #6b6b6b;
    --rule: #a08a70;
    --white: #ffffff;
  }
  * { box-sizing: border-box; margin: 0; padding: 0; }
  html, body { width: 1200px; height: 800px; overflow: hidden; }
  body { background: var(--canvas); position: relative; font-family: "Source Serif 4", Georgia, serif; }

  .voucher {
    position: absolute; left: 331px; top: 20px;
    width: 537px; height: 760px;
    background: var(--paper);
    box-shadow: 0 2px 8px rgba(0,0,0,.12);
    overflow: hidden;
  }

  .brand {
    height: 130px;
    display: flex; align-items: center; justify-content: center; gap: 12px;
  }
  .brand-dot { width: 52px; height: 52px; border-radius: 50%; background: var(--bark); }
  .brand-name { font-size: 25px; font-weight: 600; color: var(--forest); line-height: 1; }

  .hero { position: relative; height: 220px; }
  .hero-photo {
    position: absolute; inset: 0;
    background: linear-gradient(100deg, #33502a 0%, #4f6e33 40%, #a3a857 62%, #5d7a38 80%, #3d5a2c 100%);
  }
  .hero-edge { position: absolute; left: 0; bottom: -1px; width: 100%; height: 30px; }
  .hero-title {
    position: absolute; left: 0; right: 0; top: 46px; text-align: center; color: var(--white);
    font-family: "Kaushan Script", cursive; font-weight: 400;
  }
  .hero-kicker { font-size: 26px; display: block; transform: rotate(-4deg); }
  .hero-main { font-size: 58px; display: block; line-height: 1.1; margin-top: 2px; }

  .fields { padding: 36px 0 0 118px; }
  .field { display: flex; align-items: flex-end; gap: 6px; font-size: 12.5px; color: var(--bark-text); height: 30px; white-space: nowrap; }
  .field-line { width: 220px; border-bottom: 1px solid var(--rule); margin-bottom: 3px; }

  .gallery { display: flex; gap: 10px; padding: 28px 36px 0 44px; }
  .gallery-photo { flex: 1; height: 104px; }
  .gallery-photo.bedroom { background: linear-gradient(160deg, #b98a5a, #d9b48a 55%, #ece6df); }
  .gallery-photo.living { background: linear-gradient(160deg, #c9a97f, #a9835a 50%, #8a6a48); }
  .gallery-photo.bath { background: linear-gradient(160deg, #9a7458, #c49a6a 50%, #7d5f46); }

  .contact {
    display: flex; justify-content: space-between; align-items: center;
    padding: 28px 30px 0 50px;
  }
  .contact-name { font-family: "Kaushan Script", cursive; color: var(--forest); font-size: 15px; line-height: 1.25; white-space: nowrap; }
  .contact-block { font-size: 12px; color: var(--ink); line-height: 1.5; white-space: nowrap; }

  .footer-band {
    position: absolute; left: 0; bottom: 0; width: 100%; height: 56px;
    background: var(--bark); display: flex; align-items: center; justify-content: center;
    color: var(--white); font-family: "Kaushan Script", cursive; font-size: 16px; white-space: nowrap;
  }
</style>
</head>
<body>
  <main class="voucher">
    <header class="brand">
      <span class="brand-dot"></span>
      <span class="brand-name">Waldnest Baumhausdorf</span>
    </header>

    <section class="hero">
      <div class="hero-photo" role="img" aria-label="Sonniger Wald mit Baumhaus und Holztreppe"></div>
      <svg class="hero-edge" viewBox="0 0 537 30" preserveAspectRatio="none" aria-hidden="true">
        <path d="M0 14 L537 6 L537 30 L0 30 Z" fill="var(--paper)"/>
      </svg>
      <h1 class="hero-title">
        <span class="hero-kicker">Naturnah Wohnen Hotel</span>
        <span class="hero-main">Gutschein</span>
      </h1>
    </section>

    <section class="fields">
      <div class="field"><span>Gutscheinnummer:</span><span class="field-line"></span></div>
      <div class="field"><span>Ausstellungsdatum:</span><span class="field-line"></span></div>
    </section>

    <section class="gallery">
      <div class="gallery-photo bedroom" role="img" aria-label="Schlafzimmer im Baumhaus mit Holzverkleidung"></div>
      <div class="gallery-photo living" role="img" aria-label="Wohnbereich mit Fenstern zum Wald"></div>
      <div class="gallery-photo bath" role="img" aria-label="Badezimmer mit Holzwänden"></div>
    </section>

    <section class="contact">
      <p class="contact-name">Waldnest<br>Baumhausdorf</p>
      <p class="contact-block">Familie Moosbrugger<br>Lindenweg 12<br>87999 Tannried</p>
      <p class="contact-block">+ 49 (0) 1234 567890<br>info@waldnest-baumhaus.de<br>www.waldnest-baumhaus.de</p>
    </section>

    <footer class="footer-band">Entdecken Sie die Atmosphäre unserer Baumhäuser</footer>
  </main>
</body>
</html>
```